Logo and Packaging Design for Apparel and Textiles Business

Hi,

Our Business:
We are an apparel and home textiles business and would like to have a logo designed for our business as well as packaging for our products.

Products:
Initially, we are only selling Bed Sheet sets/ Towel sets and also women stoles, however later on will be expanding into apparel i.e. T-Shirts and Jeans and other clothing. Hence, packaging design should be generic enough that all of the above items can relate to it , yet it should be unique enough to leave a distinctive mark.

Design Preferences:
you can visit our website at loomvara.com.au, we have just put up the website template but have not updated it with our custom content, hence all the write-up is in Latin. However, visiting the website should give you a good idea of the color schemes to use both in Logo as well as the packaging design. The logo will be displayed on the website and hence will need to fall into contrast with existing website layout/colors. Please note the packaging design will be used to create card board packaging for all of the above products.

Business Name To be Highlighted:
Please note that business name that should be highlighted in the design for both logo and packaging is "Loomvara". If it matters in coming up with a design, the word "loomvara" is a combo of two words "loom" and "vara".

'weaving excellence'.... or 'the woven elegance'

```html
<!DOCTYPE html>
<html lang="en">
<head>
<meta charset="utf-8">
<title>Loomvara Bed Sheet Packaging – Front Panel</title>
<link rel="stylesheet" href="https://fonts.googleapis.com/css2?family=Cinzel:wght@500&family=Josefin+Sans:wght@400&display=swap">
<style>
  :root {
    --backdrop: #e1e2e4;
    --carton-grey: #5f5f5f;
    --wordmark-silver: #e6e2da;
    --accent-orange: #ec8f1f;
    --window-light: #f5921e;
    --window-dark: #7e4912;
  }

  * { margin: 0; padding: 0; box-sizing: border-box; }

  html, body {
    width: 1200px;
    height: 771px;
    overflow: hidden;
    background: var(--backdrop);
  }

  .canvas {
    position: relative;
    width: 1200px;
    height: 771px;
    background: var(--backdrop);
  }

  .front-panel {
    position: absolute;
    left: 342px;
    top: 58px;
    width: 516px;
    height: 655px;
    background: var(--carton-grey);
  }

  .brand-name {
    position: absolute;
    left: 46px;
    top: 48px;
    font-family: "Cinzel", "Trajan Pro", serif;
    font-weight: 500;
    font-size: 68px;
    line-height: 1;
    letter-spacing: 1px;
    color: var(--wordmark-silver);
    white-space: nowrap;
  }

  .product-line {
    position: absolute;
    left: 58px;
    top: 126px;
    font-family: "Josefin Sans", "Gill Sans", sans-serif;
    font-weight: 400;
    font-size: 17px;
    line-height: 1;
    letter-spacing: 6px;
    color: var(--accent-orange);
    text-transform: uppercase;
    white-space: nowrap;
  }

  .display-window {
    position: absolute;
    left: 0;
    top: 179px;
    width: 300px;
    height: 383px;
    background: linear-gradient(to right, var(--window-light) 0%, var(--window-light) 12%, var(--window-dark) 100%);
  }
</style>
</head>
<body>
  <main class="canvas">
    <section class="front-panel" aria-label="Loomvara bed sheet box, front panel">
      <h1 class="brand-name">Loomvara</h1>
      <p class="product-line">Bed Sheet</p>
      <div class="display-window" role="img" aria-label="Die-cut window showing the folded bed sheet inside"></div>
    </section>
  </main>
</body>
</html>
```